homepage design , industry automation control image

we need a design , based on our Logo image.

we focus on selling of temprature sensor ,and parts.

but need concept or image on industry automation control

we need enviroment friendly concept.

Industry/Entity Type

Industry

Number of Pages Required

5+ page

Requirements
Must have
• we need a Cartoon Image of a Temperature sensor,
• attaching a Excel file with the sensor looking.
Nice to have
• Nature image, future concept

```html
<!DOCTYPE html>
<html lang="en">
<head>
<meta charset="utf-8">
<title>Brenner Sensorik – Industry Automation Control</title>
<link href="https://fonts.googleapis.com/css2?family=Raleway:wght@400;500;600;700;800&display=swap" rel="stylesheet">
<style>
:root{
  --green:#0a870f;
  --green-dark:#066b0a;
  --lime:#8fd11b;
  --ink:#222;
  --text:#555;
  --muted:#8a8a8a;
  --footer:#2a2a2a;
  --white:#fff;
}
*{box-sizing:border-box;margin:0;padding:0}
html,body{width:1200px;height:3340px;overflow:hidden}
body{position:relative;font-family:'Raleway',sans-serif;color:var(--text);background:var(--white)}
.abs{position:absolute}
.photo{position:absolute;display:block}

/* header */
.site-header{position:absolute;left:234px;top:0;width:734px;height:78px;background:var(--white);box-shadow:0 2px 8px rgba(0,0,0,.15);z-index:5}
.brand{position:absolute;left:14px;top:12px;height:40px;display:flex;align-items:center;gap:8px;background:var(--white)}
.brand-mark{width:32px;height:32px;background:var(--green)}
.brand-name{font-weight:700;font-size:22px;color:var(--green)}
.topline{position:absolute;left:270px;top:10px;font-size:10px;color:var(--ink);display:flex;gap:26px;align-items:center}
.topline span b{font-weight:700}
.socials{display:flex;gap:5px}
.socials i{width:22px;height:22px;border:1px solid #666;border-radius:50%;display:block}
.main-nav{position:absolute;left:276px;top:50px;display:flex;gap:18px;font-size:12px;font-weight:600;color:var(--ink)}
.main-nav .active{color:var(--green)}
.search{position:absolute;right:22px;top:50px;width:12px;height:12px;border:2px solid #555;border-radius:50%}

/* hero */
.hero-panel{position:absolute;left:238px;top:214px;width:441px;height:202px;background:var(--green);padding:16px 14px;color:var(--white)}
.hero-panel h1{font-weight:800;font-size:50px;line-height:45px;letter-spacing:.5px}
.hero-panel h1 .lime{color:var(--lime)}
.hero-panel p{font-size:13.5px;line-height:17px;margin-top:10px;width:360px}
.hero-next{position:absolute;right:16px;bottom:18px;width:24px;height:24px;border:1px solid #fff;border-radius:50%}

/* about */
.about-title{left:258px;top:730px;font-weight:800;font-size:47px;line-height:44px;color:var(--ink)}
.about-title .g{color:var(--green)} .about-title .l{color:var(--lime)}
.about-text{left:258px;top:868px;width:320px;font-size:10.5px;line-height:14px}
.read-more{font-size:12px;font-weight:700;color:var(--green)}
.about-rule{left:646px;top:808px;width:80px;height:2px;background:var(--green)}

/* green bands */
.band{position:absolute;left:0;width:1200px;background:linear-gradient(135deg,#0c9a12,#067508 55%,#0a8b0e)}
.band-title{position:absolute;left:0;width:1200px;text-align:center;color:var(--white);font-weight:700;font-size:36px}
.band-sub{position:absolute;left:0;width:1200px;text-align:center;color:var(--white);font-size:16px}

/* service cards */
.svc-card{position:absolute;background:var(--white);box-shadow:0 2px 8px rgba(0,0,0,.15);text-align:center}
.svc-card h3{font-size:14px;font-weight:700;color:var(--ink);margin-top:14px}
.svc-card p{font-size:10px;line-height:12.5px;color:var(--muted);padding:6px 22px}
.btn-dark{display:inline-block;background:#444;color:#fff;font-size:11px;font-weight:600;border-radius:14px;padding:6px 22px;margin-top:4px}
.btn-lime{display:inline-block;background:var(--lime);color:#fff;font-size:11px;font-weight:600;border-radius:14px;padding:6px 24px}
.circle-arrow{position:absolute;width:46px;height:46px;border:2px solid #444;border-radius:50%;background:#fff}
.circle-arrow.light{border-color:#ccc}
.round-arrow{position:absolute;width:34px;height:34px;border:2px solid #fff;border-radius:50%}
.round-arrow.g{border-color:var(--green)}

.part-box{position:absolute;top:1897px;width:186px;height:173px;background:#fff;border-radius:4px}
.part-box .photo{left:12px;top:12px;width:162px;height:149px}

/* testimonials */
.testi{position:absolute;left:0;top:2119px;width:1200px;height:459px;background:linear-gradient(180deg,#e6e6e6,#cfcfcf 50%,#e4e4e4)}
.section-title{position:absolute;left:0;width:1200px;text-align:center;color:var(--green);font-weight:700;font-size:32px}
.sq-arrow{position:absolute;width:49px;height:48px;background:#4a4a4a}

/* blogs */
.blog-card{position:absolute;top:2680px;width:188px;height:263px;background:#fff;box-shadow:0 2px 8px rgba(0,0,0,.18)}
.blog-card .photo{left:0;top:0;width:188px;height:111px}
.blog-body{position:absolute;left:10px;top:118px;width:170px}
.blog-date{font-size:9.5px;color:var(--ink)}
.blog-cat{font-size:13px;color:var(--green);margin:2px 0 4px}
.blog-body p{font-size:9px;line-height:11.5px;color:var(--muted)}
.blog-body .read-more{font-size:9.5px;margin-top:6px;display:block;text-decoration:underline}

/* footer */
.site-footer{position:absolute;left:0;top:3076px;width:1200px;height:264px;background:var(--footer);color:#ddd}
.f-title{position:absolute;color:#fff;font-weight:700;font-size:24px}
.f-rule{position:absolute;width:52px;height:2px;background:#888}
.f-links{position:absolute;left:249px;top:3164px;list-style:none;font-size:11px;line-height:25px;color:#ddd}
.f-links li::before{content:"";display:inline-block;width:5px;height:5px;background:#ddd;border-radius:50%;margin-right:6px;vertical-align:middle}
.contact-box{position:absolute;left:677px;top:3032px;width:274px;height:308px;background:var(--green);color:#fff;padding:16px 18px;font-size:12px;line-height:16px}
.contact-box h2{font-size:29px;font-weight:700;margin-bottom:10px}
.social-row{display:flex;gap:6px;margin:12px 0 10px}
.social-row i{width:40px;height:40px;border-radius:50%;display:block}
</style>
</head>
<body>

<!-- hero -->
<div class="photo" role="img" aria-label="Engineers operating CNC machines in a factory hall" style="left:0;top:0;width:1200px;height:600px;background:linear-gradient(120deg,#cfd3d6,#9aa3a8 45%,#c7b76a 80%,#d8c24a)"></div>
<svg class="abs" style="left:0;top:520px" width="1200" height="110" viewBox="0 0 1200 110"><path d="M0 50 C300 110 700 20 1000 30 C1100 35 1160 50 1200 60 L1200 110 L0 110Z" fill="#fff"/></svg>

<header class="site-header">
  <div class="brand"><span class="brand-mark"></span><span class="brand-name">Brenner Sensorik</span></div>
  <div class="topline">
    <span><b>Phone Number:</b> 000.000.000</span>
    <span><b>Email:</b> info@brennersensorik.com</span>
    <span class="socials"><i></i><i></i><i></i></span>
  </div>
  <nav class="main-nav"><span class="active">HOME</span><span>ABOUT US</span><span>SERVICES</span><span>TESTIMONIALS</span><span>CONTACT US</span></nav>
  <span class="search"></span>
</header>

<section class="hero-panel">
  <h1><span class="lime">INDUSTRY</span><br>AUTOMATION<br>CONTROL</h1>
  <p>Lorem Ipsum is simply dummy text of the printing and typesetting industry.</p>
  <span class="hero-next"></span>
</section>

<!-- about -->
<div class="photo" role="img" aria-label="Green leaves on a vine" style="left:0;top:585px;width:300px;height:120px;background:radial-gradient(ellipse at 40% 50%,#7ccf2a,rgba(124,207,42,0) 70%)"></div>
<h2 class="abs about-title"><span class="g">BRENNER</span><br><span class="l">SENSORIK</span><br>ABOUT US</h2>
<p class="abs about-text">Lorem Ipsum is simply dummy text of the printing and typesetting industry. Lorem Ipsum has been the industry's standard dummy text ever since the 1500s, when an unknown printer took a galley of type and scrambled it to make a type specimen book.</p>
<span class="abs read-more" style="left:258px;top:945px">» Read More</span>
<span class="abs about-rule"></span>
<div class="photo" role="img" aria-label="Hand adjusting pressure gauges on brass pipework" style="left:732px;top:661px;width:323px;height:347px;background:linear-gradient(160deg,#b8b2a5,#7d6c55 55%,#a44)"></div>

<!-- services -->
<section class="band" style="top:1082px;height:309px"></section>
<h2 class="band-title" style="top:1126px">BRENNER SENSORIK SERVICES</h2>
<p class="band-sub" style="top:1172px">Lorem Ipsum is simply dummy text of the printing and typesetting industry.</p>
<svg class="abs" style="left:588px;top:1220px" width="24" height="24" viewBox="0 0 24 24" fill="none" stroke="#fff" stroke-width="2.5"><path d="M5 4l7 7 7-7M5 12l7 7 7-7"/></svg>

<div class="svc-card" style="left:263px;top:1307px;width:227px;height:300px">
  <div class="photo" role="img" aria-label="Blue temperature sensor controller" style="position:relative;width:227px;height:172px;background:linear-gradient(135deg,#9fb4c9,#2a53a0)"></div>
  <h3>Temprature Sensor</h3>
  <p>Lorem Ipsum is simply dummy text of the printing and typesetting industry. Lorem Ipsum has been the industry's standard dummy text ever since the 1500s.</p>
  <span class="btn-dark">» Read More</span>
</div>
<div class="svc-card" style="left:712px;top:1307px;width:228px;height:300px">
  <div class="photo" role="img" aria-label="Pressure gauges on pipework" style="position:relative;width:228px;height:172px;background:linear-gradient(160deg,#c0b9ab,#8a6f50 60%,#a55)"></div>
  <h3>Pressure Control</h3>
  <p>Lorem Ipsum is simply dummy text of the printing and typesetting industry. Lorem Ipsum has been the industry's standard dummy text ever since the 1500s.</p>
  <span class="btn-dark">» Read More</span>
</div>
<span class="abs" style="left:263px;top:1620px;width:677px;height:3px;background:var(--lime)"></span>
<svg class="abs" style="left:484px;top:1278px;filter:drop-shadow(0 2px 5px rgba(0,0,0,.25))" width="234" height="400" viewBox="0 0 234 400"><path d="M6 4H228V340L117 394L6 340Z" fill="#fff"/><path d="M6 340L117 394L228 340" fill="none" stroke="#8fd11b" stroke-width="3"/></svg>
<div class="photo" role="img" aria-label="Technician working at an automation control panel" style="left:490px;top:1282px;width:222px;height:212px;background:linear-gradient(135deg,#c8d2dc,#3c5f94)"></div>
<div class="abs" style="left:490px;top:1508px;width:222px;text-align:center">
  <h3 style="font-size:13.5px;font-weight:700;color:var(--ink)">Industry Automation Control</h3>
  <p style="font-size:10px;line-height:12.5px;color:var(--muted);padding:8px 24px 10px">Lorem Ipsum is simply dummy text of the printing and typesetting industry. Lorem Ipsum has been the industry's standard dummy text ever since the 1500s.</p>
  <span class="btn-lime">» Read More</span>
</div>
<span class="circle-arrow" style="left:186px;top:1484px"></span>
<svg class="abs" style="left:200px;top:1498px" width="18" height="18" viewBox="0 0 18 18" fill="none" stroke="#333" stroke-width="2"><path d="M11 3L5 9l6 6"/></svg>
<span class="circle-arrow light" style="left:970px;top:1484px"></span>
<svg class="abs" style="left:984px;top:1498px" width="18" height="18" viewBox="0 0 18 18" fill="none" stroke="#bbb" stroke-width="2"><path d="M7 3l6 6-6 6"/></svg>

<!-- parts -->
<section class="band" style="top:1730px;height:385px"></section>
<h2 class="band-title" style="top:1772px">PARTS MADE BY BRENNER SENSORIK</h2>
<p class="band-sub" style="top:1828px;font-size:13px;line-height:16px;padding:0 290px">Lorem ipsum dolor sit amet, consectetur adipisicing elit, sed do eiusmod tempor incididunt ut labore et dolore magna aliqua. Ut enim ad minim veniam, quis nostrud exercitation ullamco laboris nisi ut aliquip ex ea commodo consequat.</p>
<div class="part-box" style="left:298px"><div class="photo" role="img" aria-label="Brass valve cartridge" style="background:radial-gradient(circle,#d9a83a,#fff 70%)"></div></div>
<div class="part-box" style="left:507px"><div class="photo" role="img" aria-label="Coiled temperature probe cable" style="background:radial-gradient(circle,#aaa,#fff 70%)"></div></div>
<div class="part-box" style="left:717px"><div class="photo" role="img" aria-label="Black sensor connector part" style="background:radial-gradient(circle,#333,#fff 60%)"></div></div>
<span class="round-arrow" style="left:246px;top:1964px"></span>
<svg class="abs" style="left:256px;top:1974px" width="14" height="14" viewBox="0 0 14 14" fill="none" stroke="#fff" stroke-width="2"><path d="M9 2L4 7l5 5"/></svg>
<span class="round-arrow" style="left:918px;top:1964px"></span>
<svg class="abs" style="left:930px;top:1974px" width="14" height="14" viewBox="0 0 14 14" fill="none" stroke="#fff" stroke-width="2"><path d="M5 2l5 5-5 5"/></svg>

<!-- testimonials -->
<section class="testi" role="img" aria-label="Faded grid of client portraits"></section>
<h2 class="section-title" style="top:2196px">WHAT CLIENTS SAY</h2>
<span class="abs" style="left:575px;top:2264px;width:50px;height:3px;background:var(--green)"></span>
<div class="photo" role="img" aria-label="Portrait of client on a phone" style="left:547px;top:2296px;width:106px;height:106px;border-radius:50%;border:4px solid #fff;background:linear-gradient(160deg,#d9d9d9,#5b6670)"></div>
<p class="abs" style="left:0;top:2414px;width:1200px;text-align:center;font-size:12px;font-weight:700;color:var(--green)">CLARA WHITFIELD</p>
<p class="abs" style="left:0;top:2432px;width:1200px;text-align:center;font-size:11px;font-style:italic;color:var(--ink)">Bright Forge Inc</p>
<p class="abs" style="left:355px;top:2456px;width:490px;text-align:center;font-size:10.5px;line-height:14px;color:var(--ink)">Lorem Ipsum is simply dummy text of the printing and typesetting industry. Lorem Ipsum has been the industry's standard dummy text ever since the 1500s, when an unknown printer took a galley of type and scrambled it to make a type specimen book.</p>
<span class="sq-arrow" style="left:0;top:2349px"></span>
<svg class="abs" style="left:16px;top:2364px" width="18" height="18" viewBox="0 0 18 18" fill="none" stroke="#fff" stroke-width="2.5"><path d="M11 3L5 9l6 6"/></svg>
<span class="sq-arrow" style="left:1151px;top:2349px"></span>
<svg class="abs" style="left:1167px;top:2364px" width="18" height="18" viewBox="0 0 18 18" fill="none" stroke="#fff" stroke-width="2.5"><path d="M7 3l6 6-6 6"/></svg>

<!-- blogs -->
<h2 class="section-title" style="top:2617px">BLOGS</h2>
<article class="blog-card" style="left:298px">
  <div class="photo" role="img" aria-label="Digital thermometer on a desk" style="background:linear-gradient(135deg,#d8cfc0,#8d7a62)"></div>
  <div class="blog-body"><p class="blog-date">June 02, 2017</p><p class="blog-cat">Sample News</p><p>Lorem ipsum dolor sit amet, consectetur adipisicing elit, sed do eiusmod tempor incididunt ut labore et dolore magna aliqua. Ut enim ad minim veniam, quis nostrud exercitation ullamco laboris nisi ut aliquip ex ea commodo consequat.</p><span class="read-more">Read More</span></div>
</article>
<article class="blog-card" style="left:507px">
  <div class="photo" role="img" aria-label="Close-up of a gauge dial" style="background:linear-gradient(135deg,#b7bed6,#4b5a8a)"></div>
  <div class="blog-body"><p class="blog-date">June 02, 2017</p><p class="blog-cat">Sample News</p><p>Lorem ipsum dolor sit amet, consectetur adipisicing elit, sed do eiusmod tempor incididunt ut labore et dolore magna aliqua. Ut enim ad minim veniam, quis nostrud exercitation ullamco laboris nisi ut aliquip ex ea commodo consequat.</p><span class="read-more">Read More</span></div>
</article>
<article class="blog-card" style="left:717px">
  <div class="photo" role="img" aria-label="Pressure gauges on pipework" style="background:linear-gradient(160deg,#c0b9ab,#8a6f50 60%,#a55)"></div>
  <div class="blog-body"><p class="blog-date">June 02, 2017</p><p class="blog-cat">Sample News</p><p>Lorem ipsum dolor sit amet, consectetur adipisicing elit, sed do eiusmod tempor incididunt ut labore et dolore magna aliqua. Ut enim ad minim veniam, quis nostrud exercitation ullamco laboris nisi ut aliquip ex ea commodo consequat.</p><span class="read-more">Read More</span></div>
</article>
<span class="round-arrow g" style="left:247px;top:2795px"></span>
<svg class="abs" style="left:257px;top:2805px" width="14" height="14" viewBox="0 0 14 14" fill="none" stroke="#0a870f" stroke-width="2"><path d="M9 2L4 7l5 5"/></svg>
<span class="round-arrow g" style="left:918px;top:2795px"></span>
<svg class="abs" style="left:930px;top:2805px" width="14" height="14" viewBox="0 0 14 14" fill="none" stroke="#0a870f" stroke-width="2"><path d="M5 2l5 5-5 5"/></svg>

<!-- footer -->
<footer class="site-footer"></footer>
<h3 class="f-title" style="left:249px;top:3108px">Quick Links</h3>
<span class="f-rule" style="left:249px;top:3148px"></span>
<ul class="f-links"><li>Home</li><li>About us</li><li>Sevices</li><li>Testimonials</li><li>Blogs</li><li>Contact us</li></ul>
<h3 class="f-title" style="left:434px;top:3108px">Newsletters</h3>
<span class="f-rule" style="left:434px;top:3148px"></span>
<p class="abs" style="left:434px;top:3162px;width:210px;font-size:10.5px;line-height:13.5px;color:#ddd">Lorem Ipsum is simply dummy text of the printing and typesetting industry. Lorem Ipsum has been the industry's standard dummy text ever since the 1500s.</p>
<div class="abs" style="left:430px;top:3234px;width:210px;height:32px;border-radius:16px;background:#3a3a3a;font-size:10px;color:#aaa;padding:10px 18px">Your Email Address</div>
<div class="abs" style="left:434px;top:3282px;width:112px;height:32px;border-radius:16px;background:var(--green);color:#fff;font-size:12px;font-weight:600;text-align:center;line-height:32px">Send</div>

<aside class="contact-box">
  <h2>CONTACT US</h2>
  <p>We have a showroom in Köln with spectacular panoramic city view.</p>
  <p style="margin-top:14px">you are warmly welcome to visit our showroom and have a pleasant meeting there.</p>
  <p style="margin-top:14px"><b>Phone:</b> 000.000.000<br><b>E-Mail:</b> info@brennersensorik.com</p>
  <div class="social-row"><i style="background:#3b5998"></i><i style="background:#29a9e1"></i><i style="background:#f57d00"></i><i style="background:#dd4b39"></i></div>
  <p style="font-size:9px;line-height:12px">© Copyright <b>BRENNER SENSORIK</b>. All Rights Reserved</p>
</aside>

</body>
</html>
```